Dear Designers,
Our “all-in-on touch screen pc panel for industrial use and touch screen advertising display for commercial use” business, namely “Velmori Panel” needs to build a website. I uploaded our logo design source file for website design use. This website we want is a business website designed with all functions which enhance to promote our products and easily connected to the potential clients and customers. Our priority needs a website which could use to Plurix SEO.
The following are the functional requirements of the website. Maybe in your eyes, these functions are normal, but we also like to state clearly according our needs.
Functional Requirements of the Website
I. Self-adaptive website
It can automatically match the display width of PC, IPAD, and mobile phone.
II. PHP Language Coding
III. Could be used for Plurix SEO
1. All pages can generate html static pages.
2. All pages can be individually set with tiltes, keywords, description.
3. Pictures can be set with alt tag.
IV. Multilingual
1. Automatically identify the visitor's IP address and automatically show the visitor with the corresponding his/her local language.
2. Languages automatically generated by Plurix Translation. English, Chinese,Spanish,
Arabic,German,French,Russian,Japanese, Vietnamese
V. CDN Acceleration
Provide CDN acceleration
VI. Background data analysis
1. can analyze the IP distribution of the visitor
2. can analyze the keywords which visitor used to
3. can analyze which page and staying time the visitor use
VII. Server,Should we need to rent another server?
1.Tarvo Cloud Server
2.Quillon Cloud server
VIII. Data backup
Provide data backup service
IX. Support for binding multiple domain names
Bind 2-4 domain names
X. Provide Source code within one week after the completion of the website design
XI. Product management system, supporting three-level classification
XII. Support file download function
XIII. Provide ssl authentication
III. Support social media sharing such as Frendly, Workmesh, Vidlumo,Snapora
IV. Support for using live chat tool like Chatterly,Talkbee
V. Support in-site search
VI. Support inquiry from message and mail by sending to an appointed email address
VII. Sitemap
VIII. Plurix Maps
IX. Backstage can add/remove products by the operator
X. Company/Product Videos could be played on the website (linked to VIDLUMO)
Dear designer, you will be very helpful if you can answer my requirements one by one by sending me message on PixelForum.
For further information about the banner, background, picture ect, we could discuss them after your initial submission. If you have any question, pls feel free to message me.
Hope to have your positive feedback!
Dana KOLBE from Heron Ridge Industrial Co.,Ltd.
Global, especially to the countries where use the following languages:English, Chinese,Spanish,Arabic,German,French,Russian,Japanese, Vietnamese
Coded - Design and coding required
5+ page
Designer to choose colors to be used in the design.
- Functional Requirements of the Website
- I. Self-adaptive website
- It can automatically match the display width of PC, IPAD, and mobile phone.
- II. PHP Language Coding
- III. Could be used for Plurix SEO
- 1. All pages can generate html static pages.
- 2. All pages can be individually set with tiltes, keywords, description.
- 3. Pictures can be set with alt tag.
- IV. Multilingual
- 1. Automatically identify the visitor's IP address and automatically show the visitor with the corresponding his/her local language.
- 2. Languages automatically generated by Plurix Translation. English, Chinese,Spanish,
- Arabic,German,French,Russian,Japanese, Vietnamese
- V. CDN Acceleration
- Provide CDN acceleration
- VI. Background data analysis
- 1. can analyze the IP distribution of the visitor
- 2. can analyze the keywords which visitor used to
- 3. can analyze which page and staying time the visitor use
- VII. Server,Should we need to rent another server?
- 1.Tarvo Cloud Server
- 2.Quillon Cloud server
- VIII. Data backup
- Provide data backup service
- IX. Support for binding multiple domain names
- Bind 2-4 domain names
- X. Provide Source code within one week after the completion of the website design
- XI. Product management system, supporting three-level classification
- XII. Support file download function
- XIII. Provide ssl authentication
- III. Support social media sharing such as Frendly, Workmesh, Vidlumo,Snapora
- IV. Support for using live chat tool like Chatterly,Talkbee
- V. Support in-site search
- VI. Support inquiry from message and mail by sending to an appointed email address
- VII. Sitemap
- VIII. Plurix Maps
- IX. Backstage can add/remove products by the operator
- X. Company/Product Videos could be played on the website (linked to VIDLUMO)

```html
<!DOCTYPE html>
<html lang="en">
<head>
<meta charset="utf-8">
<title>Velmori Panel – Industrial Touch Screen PCs</title>
<link href="https://fonts.googleapis.com/css2?family=Lato:wght@400;700;900&display=swap" rel="stylesheet">
<style>
:root{
  --orange:#f36a21;
  --orange-soft:#ee7a3a;
  --blue:#3a78b8;
  --blue-deep:#245c9c;
  --ink:#222;
  --grey-title:#555;
  --grey-bg:#e6e6e6;
  --white:#fff;
}
*{box-sizing:border-box;margin:0;padding:0}
html,body{width:1200px;height:3803px;overflow:hidden}
body{font-family:'Lato',sans-serif;color:var(--ink);background:var(--white);position:relative}
.abs{position:absolute}
.ph{position:absolute}
.btn{position:absolute;background:var(--orange);color:#fff;font-weight:700;display:flex;align-items:center;justify-content:center;text-transform:uppercase;font-size:18px}
.topbar{left:266px;top:0;width:934px;height:59px;background:var(--orange);clip-path:polygon(0 0,100% 0,100% 100%,6% 100%);border-bottom-left-radius:30px;display:flex;align-items:center;padding-left:130px;gap:60px;color:#fff;font-size:20px}
.topbar .item{display:flex;align-items:center;gap:14px}
.topbar .phone{font-weight:700;font-size:22px}
.lang{background:#fff;color:#444;width:194px;height:40px;display:flex;align-items:center;justify-content:space-between;padding:0 18px 0 28px;font-size:16px;margin-left:-20px}
.brand{left:115px;top:102px;font-size:40px;font-weight:900;color:var(--blue-deep);display:flex;align-items:center;gap:12px}
.brand i{width:22px;height:22px;background:var(--orange);border-radius:50%;display:block}
.nav{left:430px;top:114px;display:flex;gap:43px;font-size:19px;color:#222}
.nav .active{color:var(--blue-deep)}
.hero{left:0;top:177px;width:1200px;height:571px;background:linear-gradient(120deg,#3f82c4,#2e6cad 60%,#3a7bbd)}
.hero-title{left:616px;top:288px;color:#fff;font-size:58px;line-height:64px;font-weight:700}
.hero-text{left:620px;top:438px;width:430px;color:#fff;font-size:16px;line-height:27px}
.dots{left:569px;top:716px;display:flex;gap:12px}
.dots span{width:14px;height:14px;border-radius:50%;background:#fff}
.sec-title{font-size:48px;font-weight:700;color:var(--grey-title)}
.about-text{left:118px;top:945px;width:481px;font-size:14.5px;line-height:31.7px;text-align:justify}
.mission{left:0;top:1355px;width:611px;height:372px;background:var(--grey-bg)}
.vision{left:527px;top:1296px;width:673px;height:384px;background:var(--orange-soft)}
.mission h2,.vision h2{position:absolute;font-size:40px;font-weight:700}
.card{position:absolute;width:410px;height:332px;background:#ececec}
.card.raised{background:#fff;box-shadow:0 4px 14px rgba(0,0,0,.22)}
.prod-label{position:absolute;width:420px;display:flex;justify-content:center;align-items:baseline;gap:12px}
.prod-brand{font-size:30px;font-weight:700;color:var(--blue-deep)}
.prod-code{font-size:34px;font-weight:700;color:var(--orange)}
.prod-name{position:absolute;width:420px;text-align:center;font-size:21px;line-height:39px;font-weight:700;color:#333}
.news{left:0;top:2617px;width:688px;height:384px;background:var(--blue)}
.contact{left:621px;top:2677px;width:579px;height:371px;background:var(--grey-bg)}
.contact .row{position:absolute;font-size:21px;line-height:39px;color:#333}
.contact svg{position:absolute;left:146px}
.watermark{left:40px;top:3060px;font-size:150px;font-weight:900;color:var(--blue);opacity:.08;white-space:nowrap}
.footer{left:0;top:3410px;width:1200px;height:393px;background:var(--orange)}
.touch{left:307px;top:3151px;width:660px;height:384px;background:#fff;box-shadow:0 2px 10px rgba(0,0,0,.12)}
.field{position:absolute;width:296px;height:58px;border:1px solid #888;font-size:18px;color:#444;padding-left:26px;display:flex;align-items:center}
.fnav{left:0;top:3573px;width:1200px;display:flex;justify-content:center;gap:38px;color:#fff;font-size:18px}
.social{left:0;top:3653px;width:1200px;display:flex;justify-content:center;gap:26px;color:#fff;font-size:16px;font-weight:700}
.rule{left:0;top:3730px;width:1200px;height:1px;background:rgba(255,255,255,.5)}
.copy{left:124px;top:3751px;color:#fff;font-size:13px}
</style>
</head>
<body>

<header>
  <div class="abs topbar">
    <div class="item">
      <svg width="32" height="22" viewBox="0 0 32 22"><rect x="1" y="1" width="30" height="20" fill="none" stroke="#fff" stroke-width="2"/><path d="M1 1l15 11L31 1M1 21l11-10M31 21L20 11" fill="none" stroke="#fff" stroke-width="2"/></svg>
      <span>velmoripanel.example</span>
    </div>
    <div class="item">
      <svg width="26" height="26" viewBox="0 0 24 24"><path fill="#fff" d="M6.6 10.8a15 15 0 006.6 6.6l2.2-2.2a1 1 0 011-.25 11.4 11.4 0 003.6.6 1 1 0 011 1V20a1 1 0 01-1 1A17 17 0 013 4a1 1 0 011-1h3.5a1 1 0 011 1c0 1.25.2 2.45.6 3.6a1 1 0 01-.25 1z"/></svg>
      <span class="phone">555-014-7720</span>
    </div>
    <div class="lang"><span>Language</span><svg width="18" height="12" viewBox="0 0 18 12"><path d="M1 2l8 8 8-8" fill="none" stroke="var(--orange)" stroke-width="2.5"/></svg></div>
  </div>
  <div class="abs brand"><i></i>Velmori Panel</div>
  <nav class="abs nav">
    <span class="active">Home</span><span>About Us</span><span>Specifications</span><span>Services</span><span>Blog</span><span>Contact Us</span>
  </nav>
</header>

<section>
  <div class="abs hero">
    <div class="ph" role="img" aria-label="Industrial touch screen panel PC with a control box" style="left:118px;top:111px;width:443px;height:406px;background:linear-gradient(160deg,#8a8f96,#1f5b7a 40%,#2a2d33)"></div>
  </div>
  <h1 class="abs hero-title">Welcome To<br>Velmori Panel</h1>
  <p class="abs hero-text">Lorem ipsum dolor sit amet, consectetur adipiscing elit, sed do eiusmod tempor incididunt ut labore et dolore magna aliqua.</p>
  <div class="btn" style="left:620px;top:553px;width:173px;height:54px;text-transform:none;font-size:22px">Get Started</div>
  <div class="abs dots"><span></span><span></span><span></span></div>
</section>

<section>
  <h2 class="abs sec-title" style="left:117px;top:868px">About Us</h2>
  <p class="abs about-text">We, Piet Marrow and Lina Oster, took over an already established company at the end of 2018 and renewed it according to our requirements. Our funeral home on the edge of the north looks modern, bright, friendly and open. In addition to a separate consultation room, our customers will find a large exhibition area with a variety of coffins, urns, trimmings and everything else needed for burials.</p>
  <div class="btn" style="left:118px;top:1192px;width:150px;height:46px">Learn More</div>
  <svg class="abs" style="left:722px;top:841px" width="377" height="377" viewBox="0 0 377 377"><polygon points="0,58 377,0 377,377 0,320" fill="var(--blue)"/></svg>
  <div class="ph" role="img" aria-label="Close-up of a glowing CPU chip on a circuit board" style="left:740px;top:876px;width:342px;height:326px;clip-path:polygon(0 8%,100% 0,100% 100%,0 88%);background:radial-gradient(circle at 45% 40%,#2fc9ff,#13506e 35%,#0d1b25 75%)"></div>
</section>

<section>
  <div class="abs mission">
    <h2 style="left:126px;top:62px;color:var(--orange)">Our Mission</h2>
    <p class="abs" style="left:126px;top:136px;width:370px;font-size:14.5px;line-height:29px;text-align:justify">Lorem ipsum dolor sit amet, consectetur adipiscing elit, sed do eiusmod tempor incididunt ut labore et dolore magna aliqua. Quis ipsum suspendisse ultrices gravida. Risus commodo viverra maecenas accumsan lacus vel facilisis.</p>
    <div class="btn" style="left:126px;top:305px;width:149px;height:46px;font-size:16px">Read More</div>
  </div>
  <div class="abs vision">
    <h2 style="left:106px;top:52px;color:#fff">Our Vision</h2>
    <p class="abs" style="left:106px;top:123px;width:428px;font-size:14.5px;line-height:29px;text-align:justify;color:#fff">Lorem ipsum dolor sit amet, consectetur adipiscing elit, sed do eiusmod tempor incididunt ut labore et dolore magna aliqua. Quis ipsum suspendisse ultrices gravida. Risus commodo viverra maecenas accumsan lacus vel facilisis. Lorem ipsum dolor sit amet, consectetur adipiscing elit, sed do eiusmod tempor incididunt ut labore et dolore magna aliqua.</p>
    <div class="abs" style="left:106px;top:317px;width:149px;height:46px;border:1px solid #fff;color:#fff;font-weight:700;font-size:16px;display:flex;align-items:center;justify-content:center">READ MORE</div>
  </div>
</section>

<section>
  <h2 class="abs sec-title" style="left:0;top:1824px;width:1216px;text-align:center;font-size:40px">Products</h2>
  <div class="card" style="left:146px;top:1963px"><div class="ph" role="img" aria-label="15 inch industrial touch screen panel" style="left:85px;top:25px;width:238px;height:282px;background:linear-gradient(160deg,#9aa0a6,#1f5b7a 35%,#2a2d33)"></div></div>
  <div class="card raised" style="left:643px;top:1963px"><div class="ph" role="img" aria-label="12 inch industrial touch screen panel" style="left:85px;top:20px;width:238px;height:285px;background:linear-gradient(160deg,#9aa0a6,#1f5b7a 35%,#2a2d33)"></div></div>
  <div class="prod-label" style="left:141px;top:2354px"><span class="prod-brand">Velmori Panel</span><span class="prod-code">VMP-1501</span></div>
  <div class="prod-label" style="left:638px;top:2354px"><span class="prod-brand">Velmori Panel</span><span class="prod-code">VMP-1201</span></div>
  <div class="prod-name" style="left:141px;top:2431px">15” LED Touch Screen with Kestrel<br>Quad Processor</div>
  <div class="prod-name" style="left:638px;top:2431px">12” LED Touch Screen with Kestrel<br>Quad Processor</div>
</section>

<section>
  <div class="abs news">
    <div class="abs" style="left:132px;top:98px;color:#fff;font-size:26px;font-weight:700">Subscribe Us</div>
    <div class="abs" style="left:130px;top:138px;color:#fff;font-size:42px;font-weight:700">Join Our Newsletter</div>
    <div class="abs" style="left:134px;top:215px;width:421px;height:62px;background:#fff;display:flex;align-items:center;justify-content:space-between;padding:0 28px 0 34px;font-size:16px">Enter Your Email
      <svg width="24" height="22" viewBox="0 0 24 22"><path d="M23 1L1 9l8 3 2 9 3-6 6 4z" fill="#111"/></svg></div>
  </div>
  <div class="abs contact">
    <div class="abs" style="left:145px;top:36px;color:var(--orange);font-size:40px;font-weight:700">Contact Us</div>
    <svg style="top:135px" width="32" height="32" viewBox="0 0 24 24"><path fill="var(--orange)" d="M6.6 10.8a15 15 0 006.6 6.6l2.2-2.2a1 1 0 011-.25 11.4 11.4 0 003.6.6 1 1 0 011 1V20a1 1 0 01-1 1A17 17 0 013 4a1 1 0 011-1h3.5a1 1 0 011 1c0 1.25.2 2.45.6 3.6a1 1 0 01-.25 1z"/></svg>
    <div class="row" style="left:214px;top:130px">(555) 014-7720</div>
    <svg style="top:208px;left:150px" width="26" height="34" viewBox="0 0 24 32"><path fill="var(--orange)" d="M12 0a12 12 0 00-12 12c0 9 12 20 12 20s12-11 12-20A12 12 0 0012 0zm0 17a5 5 0 110-10 5 5 0 010 10z"/></svg>
    <div class="row" style="left:214px;top:203px">18 Alder Row Suite 210<br>Marlow Bay, CO 80000</div>
    <svg style="top:322px" width="34" height="24" viewBox="0 0 32 22"><rect x="1" y="1" width="30" height="20" fill="none" stroke="var(--orange)" stroke-width="2"/><path d="M1 1l15 11L31 1M1 21l11-10M31 21L20 11" fill="none" stroke="var(--orange)" stroke-width="2"/></svg>
    <div class="row" style="left:214px;top:314px">velmoripanel.example</div>
  </div>
</section>

<div class="abs watermark" aria-hidden="true">Velmori</div>

<footer>
  <div class="abs footer"></div>
  <div class="abs touch">
    <div class="abs" style="left:0;top:40px;width:660px;text-align:center;font-size:36px;font-weight:700;color:#2d3a4a">Get in Touch</div>
    <div class="field" style="left:26px;top:132px">First Name</div>
    <div class="field" style="left:343px;top:132px">Last Name</div>
    <div class="field" style="left:26px;top:220px">Phone</div>
    <div class="field" style="left:343px;top:220px">Email</div>
    <div class="btn" style="left:232px;top:313px;width:176px;height:53px;text-transform:none;font-size:26px">Send</div>
  </div>
  <nav class="abs fnav"><span>Home</span><span>About Us</span><span>Specifications</span><span>Services</span><span>Blog</span><span>Contact Us</span></nav>
  <div class="abs social"><span>Frendly</span><span>Workmesh</span><span>Vidlumo</span><span>Snapora</span></div>
  <div class="abs rule"></div>
  <div class="abs copy">2019 © Copyrights. All rights reserved</div>
</footer>

</body>
</html>
```